Candle company needs a label for candle

Looking for a designer to create my candle label. I am going to attach a few pictures of my vision for the label as well as my Company Logo and jar I have puchased. I'm going for the modern rustic feel but you are the designer and have full trust in your abilities. The label is going to be printed on Kraft paper (2x3) so looking for the font to be black. The candle label MUST include the following information:
Candle Birchway Co.
NO. 01: Eucalyptus + Spearmint
Handmade In NJ
Soy Wax
9oz

Industry/Entity Type

Candle Industry

Colors

Designer to choose colors to be used in the design.

Requirements
Should not have
• Any images

```html
<!DOCTYPE html>
<html lang="en">
<head>
<meta charset="utf-8">
<title>Candle Birchway Co. — Label Options</title>
<link href="https://fonts.googleapis.com/css2?family=Josefin+Sans:wght@300;400&display=swap" rel="stylesheet">
<style>
  :root {
    --page: #ffffff;
    --label-ink: #231f20;
    --gold: #a97f52;
    --gold-band: #a87d4f;
  }
  * { box-sizing: border-box; margin: 0; padding: 0; }
  html, body {
    width: 1200px; height: 1200px; overflow: hidden;
    background: var(--page);
    font-family: "Josefin Sans", sans-serif;
  }
  .sheet {
    position: relative; width: 1200px; height: 1200px;
    display: flex; align-items: center; justify-content: center; gap: 40px;
  }
  .label {
    position: relative; width: 540px; height: 360px;
    background: var(--label-ink); color: var(--gold);
  }
  .label__frame { position: absolute; inset: 0; }
  .brand {
    position: absolute; left: 0; right: 0; top: 78px;
    display: flex; align-items: center; justify-content: center; gap: 12px;
  }
  .brand__mark {
    width: 12px; height: 12px; background: var(--gold);
  }
  .brand__name {
    font-weight: 400; font-size: 30px; line-height: 36px;
    color: var(--gold);
  }
  .scent-number {
    position: absolute; left: 36px; top: 190px;
    font-weight: 300; font-size: 18px; letter-spacing: -0.5px;
  }
  .scent-name {
    position: absolute; left: 30px; right: 30px; top: 224px;
    text-align: center; font-weight: 300; font-size: 23px; letter-spacing: 2px;
  }
  .details {
    position: absolute; left: 0; right: 0; top: 284px;
    text-align: center; font-weight: 400; font-size: 14px; letter-spacing: 0.8px;
  }
  .weight {
    position: absolute; left: 0; right: 0; top: 306px;
    text-align: center; font-weight: 300; font-size: 28px;
  }
  .label--banded .scent-number,
  .label--banded .scent-name { color: var(--label-ink); }
</style>
</head>
<body>
<main class="sheet">

  <section class="label label--outlined">
    <svg class="label__frame" width="540" height="360" viewBox="0 0 540 360" aria-hidden="true">
      <path d="M100 200 H498 V272 H38 V224" fill="none" stroke="var(--gold)" stroke-width="3"/>
    </svg>
    <div class="brand">
      <span class="brand__mark" aria-hidden="true"></span>
      <h1 class="brand__name">Candle Birchway Co.</h1>
    </div>
    <p class="scent-number">NO. 01</p>
    <p class="scent-name">EUCALYPTUS + SPEARMINT</p>
    <p class="details">Handmade In NJ • Soy Wax</p>
    <p class="weight">9oz</p>
  </section>

  <section class="label label--banded">
    <svg class="label__frame" width="540" height="360" viewBox="0 0 540 360" aria-hidden="true">
      <rect x="30" y="186" width="480" height="92" fill="var(--gold-band)"/>
      <path d="M98 196 H500 V268 H42 V222" fill="none" stroke="var(--label-ink)" stroke-width="3"/>
    </svg>
    <div class="brand">
      <span class="brand__mark" aria-hidden="true"></span>
      <h1 class="brand__name">Candle Birchway Co.</h1>
    </div>
    <p class="scent-number">NO. 01</p>
    <p class="scent-name">EUCALYPTUS + SPEARMINT</p>
    <p class="details">Handmade In NJ • Soy Wax</p>
    <p class="weight">9oz</p>
  </section>

</main>
</body>
</html>
```